Ferris Contracting LLC Business Card Design

I am looking for a creative and unique business card design. We are a commercial construction general contractor. With the name "FERRIS" Contracting, I am hoping to see some neat designs that correlate with the name.

```html
<!DOCTYPE html>
<html lang="en">
<head>
<meta charset="UTF-8">
<title>Ferris Contracting LLC – Business Card</title>
<link href="https://fonts.googleapis.com/css2?family=Michroma&display=swap" rel="stylesheet">
<style>
  :root {
    --stage: #3a3b3e;
    --stage-light: #55575b;
    --card: #000000;
    --brand-blue: #2a8fd8;
    --steel-grey: #5b5e64;
    --text-grey: #c9cacc;
  }
  * { box-sizing: border-box; margin: 0; padding: 0; }
  html, body { width: 1200px; height: 900px; overflow: hidden; }
  body {
    background: radial-gradient(ellipse at 60% 30%, var(--stage-light), var(--stage) 70%);
    font-family: "Michroma", sans-serif;
    position: relative;
  }
  .card {
    position: absolute;
    left: 260px;
    width: 680px;
    height: 388px;
    background: var(--card);
    box-shadow: 0 10px 28px rgba(0,0,0,0.55);
    overflow: hidden;
  }
  .card--front { top: 42px; }
  .card--back  { top: 470px; }

  .brand {
    position: absolute;
    inset: 0;
    display: flex;
    align-items: center;
    justify-content: center;
    gap: 32px;
  }
  .brand__disc {
    width: 170px;
    height: 170px;
    border-radius: 50%;
    background: var(--steel-grey);
    flex: none;
  }
  .brand__name {
    color: var(--brand-blue);
    font-size: 38px;
    line-height: 1.35;
    letter-spacing: 2px;
    text-transform: uppercase;
  }

  .person {
    position: absolute;
    left: 52px;
    top: 92px;
  }
  .person__name {
    color: var(--brand-blue);
    font-size: 24px;
    font-weight: 400;
    letter-spacing: 1px;
    text-transform: uppercase;
  }
  .person__role {
    margin-top: 10px;
    color: var(--text-grey);
    font-size: 18px;
    letter-spacing: 1px;
    text-transform: uppercase;
  }

  .contact {
    position: absolute;
    left: 170px;
    bottom: 44px;
    list-style: none;
  }
  .contact__item {
    display: flex;
    align-items: center;
    gap: 18px;
    color: var(--text-grey);
    font-size: 16px;
    letter-spacing: 1px;
    text-transform: uppercase;
    line-height: 32px;
  }
  .contact__icon {
    width: 16px;
    height: 16px;
    fill: var(--brand-blue);
    flex: none;
  }
</style>
</head>
<body>

  <section class="card card--front" aria-label="Card front">
    <div class="brand">
      <span class="brand__disc"></span>
      <span class="brand__name">Ferris<br>Contracting</span>
    </div>
  </section>

  <section class="card card--back" aria-label="Card back">
    <div class="person">
      <h1 class="person__name">Mr. Marcus Tolland</h1>
      <p class="person__role">Founder</p>
    </div>

    <ul class="contact">
      <li class="contact__item">
        <svg class="contact__icon" viewBox="0 0 24 24" aria-hidden="true"><path d="M6.6 10.8a15.1 15.1 0 0 0 6.6 6.6l2.2-2.2c.3-.3.7-.4 1-.2 1.1.4 2.3.6 3.6.6.6 0 1 .4 1 1V20c0 .6-.4 1-1 1A17 17 0 0 1 3 4c0-.6.4-1 1-1h3.5c.6 0 1 .4 1 1 0 1.3.2 2.5.6 3.6.1.3 0 .7-.2 1z"/></svg>
        <span>(555) 014-2738</span>
      </li>
      <li class="contact__item">
        <svg class="contact__icon" viewBox="0 0 24 24" aria-hidden="true"><path d="M2 5h20v14H2z"/><path d="M2 5l10 8 10-8" fill="none" stroke="#000" stroke-width="1.6"/></svg>
        <span>info@ferrisconstruction.com</span>
      </li>
      <li class="contact__item">
        <svg class="contact__icon" viewBox="0 0 24 24" aria-hidden="true"><path d="M12 2a10 10 0 1 0 5 18.7l-1-1.7A8 8 0 1 1 20 12v1a2 2 0 0 1-4 0V7h-2v1a5 5 0 1 0 .8 6.8A4 4 0 0 0 22 13v-1A10 10 0 0 0 12 2zm0 13a3 3 0 1 1 0-6 3 3 0 0 1 0 6z"/></svg>
        <span>www.ferrisconstruction.com</span>
      </li>
    </ul>
  </section>

</body>
</html>
```